Realtor and Real Estate Business Card

I need a business card that is a cross between a realtor's business card and that of a CEO of a property management group. Realtor cards are focused on the selling while property management is not. QR code must be included. My picture is included, but I do not need to have that. I prefer no picture, but a lot realtor cards have them so it is okay, and maybe better, if you do you use the image. It is probably best to crop out the background and use just my image or head. Need two designs with the two different logos swapped out. All the logo images files are in the zip drive for you to pick which file you need.

I want a card that is sales-oriented but something a non-sales person would use at the same time. It is a delicate balance. I like bold and eye-catching designs, but that is not necessary.

Phone number 4823107965
Email is marcus@zephyrlandholdings.com

Industry/Entity Type

Real Estate

Contact Information for Business Card

See brief for all details

Requirements
Must have
• Logos and the back of the card must have logo on it. QR code must be on
Nice to have
• I am indifferent about using my image
Should not have
• Mailing address

```html
<!DOCTYPE html>
<html lang="en">
<head>
<meta charset="utf-8">
<title>Zephyr Business Cards</title>
<link href="https://fonts.googleapis.com/css2?family=Montserrat:wght@400;500;700;800&display=swap" rel="stylesheet">
<style>
  :root{
    --bg:#eef0f2;
    --card:#ffffff;
    --green:#0b5e3c;
    --grey:#9b9b9b;
    --grey-soft:#e4e4e4;
    --ink:#2a2a2a;
    --blue:#1c60b8;
    --blue-soft:#2f74c8;
    --muted:#6f6f6f;
    --qr-fill:#f1f3f6;
    --qr-line:#c9ced6;
  }
  *{box-sizing:border-box;margin:0;padding:0}
  html,body{width:1200px;height:873px;overflow:hidden;background:var(--bg);font-family:"Montserrat",sans-serif}
  .stage{position:relative;width:1200px;height:873px}
  .card{position:absolute;width:530px;height:304px;background:var(--card);border-radius:6px;box-shadow:0 10px 30px rgba(0,0,0,.18);overflow:hidden}

  /* green card */
  .card--home{left:45px;top:285px}
  .home__socials{position:absolute;left:26px;top:70px;display:flex;flex-direction:column;gap:14px}
  .home__social{width:26px;height:26px;border-radius:6px;background:linear-gradient(#c4c4c4,#8c8c8c)}
  .home__rule{position:absolute;left:72px;top:30px;width:7px;height:244px;background:var(--green)}
  .home__info{position:absolute;left:100px;top:38px}
  .brand{display:flex;align-items:center;gap:8px}
  .brand__mark{width:14px;height:14px;background:var(--green)}
  .brand__name{font-weight:800;font-size:34px;color:var(--green);letter-spacing:.5px;line-height:1}
  .brand__sub{font-size:11px;letter-spacing:8px;color:var(--grey);margin:6px 0 0 22px;font-weight:500}
  .home__name{margin-top:22px;font-weight:800;font-size:21px;color:var(--ink);letter-spacing:.5px}
  .home__title{margin-top:6px;font-size:10px;color:var(--green);font-weight:500}
  .contact{list-style:none;margin-top:10px}
  .contact li{display:flex;align-items:center;gap:8px;font-size:9.5px;color:var(--muted);margin-bottom:6px}
  .contact svg{width:10px;height:10px;flex:none}
  .home__art{position:absolute;left:300px;top:205px;width:175px;height:75px;border-radius:4px;background:linear-gradient(90deg,var(--grey-soft),#cfd8d3)}
  .home__band{position:absolute;right:0;top:40px;width:36px;height:264px;background:var(--green);border-top-left-radius:30px}

  /* blue card */
  .card--group{left:625px;top:285px}
  .group__arc{position:absolute;left:-210px;top:-60px;width:420px;height:424px;border-radius:50%;background:linear-gradient(160deg,var(--blue-soft),var(--blue))}
  .group__info{position:absolute;left:240px;top:52px}
  .group__brand{display:flex;align-items:center;gap:10px}
  .group__mark{width:34px;height:34px;border:2px solid var(--blue);border-radius:50%}
  .group__brandname{font-weight:500;font-size:20px;color:var(--blue);letter-spacing:1px;line-height:1.05}
  .group__brandname span{display:block;font-size:9px;color:var(--muted);letter-spacing:1.5px}
  .group__name{margin-top:30px;font-weight:800;font-size:22px;color:var(--ink)}
  .group__title{margin-top:4px;font-size:12px;color:var(--blue);font-weight:500}
  .group__info .contact{margin-top:14px}
  .group__info .contact li{font-size:10px}
  .qr{position:absolute;left:446px;top:214px;width:62px;height:62px;border-radius:4px;background:var(--qr-fill);border:2px solid var(--qr-line)}
</style>
</head>
<body>
<main class="stage">

  <section class="card card--home" aria-label="Zephyr Home Sales business card">
    <div class="home__socials">
      <span class="home__social"></span><span class="home__social"></span>
      <span class="home__social"></span><span class="home__social"></span>
    </div>
    <div class="home__rule"></div>
    <div class="home__info">
      <div class="brand"><span class="brand__mark"></span><span class="brand__name">Zephyr</span></div>
      <div class="brand__sub">HOME SALES</div>
      <h1 class="home__name">MARCUS DELANE</h1>
      <p class="home__title">Chief Executive Officer</p>
      <ul class="contact">
        <li><svg viewBox="0 0 10 10"><path d="M2 1h2l1 2-1 1a5 5 0 0 0 2 2l1-1 2 1v2c-4 0-7-3-7-7z" fill="#333"/></svg>+4823107965</li>
        <li><svg viewBox="0 0 10 10"><rect x=".5" y="1.5" width="9" height="7" fill="none" stroke="#333"/><path d="M1 2l4 3 4-3" fill="none" stroke="#333"/></svg>marcus@zephyrlandholdings.com</li>
      </ul>
    </div>
    <div class="home__art" role="img" aria-label="Area for the brand's decorative rooftop artwork"></div>
    <div class="home__band"></div>
  </section>

  <section class="card card--group" aria-label="Zephyr Land Holdings business card">
    <div class="group__arc" role="img" aria-label="Blue arc holding a faint building outline decoration"></div>
    <div class="group__info">
      <div class="group__brand">
        <span class="group__mark"></span>
        <div class="group__brandname">ZEPHYR<span>LAND HOLDINGS</span></div>
      </div>
      <h1 class="group__name">Marcus Delane</h1>
      <p class="group__title">Chief Executive Officer</p>
      <ul class="contact">
        <li><svg viewBox="0 0 10 10"><path d="M2 1h2l1 2-1 1a5 5 0 0 0 2 2l1-1 2 1v2c-4 0-7-3-7-7z" fill="#333"/></svg>+4823107965</li>
        <li><svg viewBox="0 0 10 10"><rect x=".5" y="1.5" width="9" height="7" fill="none" stroke="#333"/><path d="M1 2l4 3 4-3" fill="none" stroke="#333"/></svg>marcus@zephyrlandholdings.com</li>
      </ul>
    </div>
    <div class="qr" role="img" aria-label="QR code area linking to the company website"></div>
  </section>

</main>
</body>
</html>
```